New Business Cards for Torvin Group

We need a new Business Card to compliment our new logo. We are a vibrant design, manufacture and install business providing recreation areas, public parks and Municipal spaces. We want business cards that are classy, modern and clean.

We have recently changed our logo, and are celebrating our 40th anniversary. We want business cards with a new modern design to reflect our status.

Target Market(s)

Customers

Contact Information for Business Card

We need all the details of our 3 offices as per the business card attached. Please disregard the old logo on the business card, the other three files show our new logo.

Requirements
Must have
• All info as per attached business card but with new logo.
Nice to have

```html
<!DOCTYPE html>
<html lang="en">
<head>
<meta charset="utf-8">
<title>Torvin Group – Business Card</title>
<link rel="stylesheet" href="https://fonts.googleapis.com/css2?family=Exo+2:wght@500;600;700&family=Open+Sans:wght@400;600&display=swap">
<style>
  :root {
    --brand-red: #e5303c;
    --brand-red-dark: #c81e2b;
    --ink-grey: #4a4a4c;
    --text-grey: #3d3d3f;
    --card-white: #ffffff;
    --backdrop: #d6d6d6;
  }
  * { box-sizing: border-box; margin: 0; padding: 0; }
  html, body { width: 1200px; height: 900px; overflow: hidden; }
  body {
    background: var(--backdrop);
    display: flex; align-items: center; justify-content: center;
    font-family: "Open Sans", Arial, sans-serif;
  }
  .business-card {
    position: relative;
    width: 1050px; height: 600px;
    background: var(--card-white);
    overflow: hidden;
    box-shadow: 0 6px 18px rgba(0,0,0,.18);
  }
  .card-swoosh { position: absolute; inset: 0; }
  .brand {
    position: absolute; top: 58px; left: 590px;
    display: flex; align-items: center; gap: 22px;
  }
  .brand-dot {
    width: 150px; height: 150px; border-radius: 50%;
    background: var(--brand-red);
  }
  .brand-name {
    font-family: "Exo 2", Arial, sans-serif; font-weight: 700;
    font-size: 58px; line-height: .95; color: var(--ink-grey);
    letter-spacing: 1px; text-transform: uppercase;
  }
  .holder { position: absolute; top: 190px; left: 62px; }
  .holder-name {
    font-family: "Exo 2", Arial, sans-serif; font-weight: 600;
    font-size: 34px; color: var(--brand-red); letter-spacing: 1px;
  }
  .holder-title {
    font-family: "Exo 2", Arial, sans-serif; font-weight: 500;
    font-size: 22px; color: var(--text-grey); margin-top: 2px; letter-spacing: .5px;
  }
  .holder-contact { margin-top: 26px; font-size: 21px; line-height: 1.45; color: var(--text-grey); }
  .office { position: absolute; font-size: 19px; line-height: 1.42; color: var(--text-grey); }
  .office-title {
    font-family: "Exo 2", Arial, sans-serif; font-weight: 500;
    font-size: 25px; color: var(--brand-red); margin-bottom: 2px;
  }
  .office--head { top: 400px; left: 62px; }
  .office--dubai { top: 235px; left: 470px; }
  .office--qatar { top: 225px; left: 770px; }
  .web-address {
    position: absolute; left: 790px; top: 470px;
    font-size: 20px; font-weight: 600; color: var(--card-white);
    transform: rotate(-23deg); transform-origin: left center;
    letter-spacing: .5px;
  }
</style>
</head>
<body>
  <article class="business-card">
    <svg class="card-swoosh" viewBox="0 0 1050 600" aria-hidden="true">
      <path d="M330 600 C560 520 820 430 1050 330 L1050 338 C820 440 570 530 360 600 Z" fill="var(--ink-grey)"/>
      <path d="M380 600 C600 530 830 450 1050 360 L1050 600 Z" fill="var(--brand-red)"/>
      <path d="M420 600 C620 540 840 470 1050 395 L1050 402 C840 478 630 548 450 600 Z" fill="var(--card-white)"/>
      <path d="M470 600 C650 550 860 485 1050 420 L1050 600 Z" fill="var(--brand-red-dark)" opacity=".35"/>
    </svg>

    <div class="brand">
      <span class="brand-dot"></span>
      <span class="brand-name">Torvin<br>Group</span>
    </div>

    <section class="holder">
      <h1 class="holder-name">MAREK DOLAND</h1>
      <p class="holder-title">MANAGING PARTNER</p>
      <p class="holder-contact">M: +971[0] 50 738 4420<br>marek@torvingroup.com</p>
    </section>

    <section class="office office--head">
      <h2 class="office-title">Head Office</h2>
      P.O. Box 41822 Abu Dhabi, U.A.E.<br>
      T: +971 [0] 2 5173920<br>
      F: +971 [0] 2 5173921<br>
      sales@torvingroup.com
    </section>

    <section class="office office--dubai">
      <h2 class="office-title">Dubai Office</h2>
      P.O. Box 508317 Dubai U.A.E.<br>
      T: +971 [0] 4 3862054<br>
      F: +971 [0] 4 3862055<br>
      sales@torvingroup.com
    </section>

    <section class="office office--qatar">
      <h2 class="office-title">Qatar Office</h2>
      P.O. Box 27389 Doha Qatar<br>
      T: +974 44917036<br>
      F: +974 44917037<br>
      sales@torvingroup.com
    </section>

    <p class="web-address">www.torvingroup.com</p>
  </article>
</body>
</html>
```